Design my site www.marquetally.example

So here is what I am thinking in terms of design:

https://plovex.example

https://www.caldorejet.example

http://brevon.example/harbor-spire-plaza/

I want the theme to be white and blue (royal blue). I attached a paint picture of what I would like the site to look like in terms of placing the text. Generally, what I like about the sites above is that they are simple, you can navigate easily and have some kind of idea of what's going on by looking at the center (picture and motto). Let's establish a clear understanding of how the functional part of the site would look like. Please see the picture attached.

I want to keep it simple: On top would be the Name 'MARQUE tally", somewhere to the right on top on the page would be 'Sign in" button.

In the center would be a picture (maybe a video) with the Motto (on top of it all in capital) OBSERVE NAVIGATE DECIDE and below would be the "sign up now"

Below the picture (like on brevon.example site) or to the left on top of the page would be "About Us', "Press" "Contact Us' buttons.

Then once the user gets to his page his got 3 tabs " Press Headlines", "Events", " Briefings".

we would keep the same format I only have on the site, but separate for every Tab.

I do not want the user to get distracted. I also want him to be able to access the page though mobile phone and be able to get automatic updates just like Fennix Pings without having to sign in daily.

The landing page must be minimalist yet with business/corporate feel where users can navigate easily and a "what you see is what you get" approach. You want an image or video (personally I prefer the video.. it does capture the users attention instantly, as long as it is an interesting video), with your taglines in it.

Sections available to public: About Us, Contact Us, Landing Page with Signup Option

Private: Public Sections + User Account Page, Tabs for (Events, Press Headlines, Briefings)

Target Market(s)

PR/media monitoring/diplomatic community

Coding

Coded - Design and coding required

Number of Pages Required

1 page

Font styles to use
Serif
Sans Serif

Colors
0255a3
ec1f27

Requirements
Must have
• a simple landing page, that is user friendly.
Nice to have
• a video with the explanation of how to navigate the site
Should not have
• too many colors, graphs etc.

```html
<!DOCTYPE html>
<html lang="en">
<head>
<meta charset="utf-8">
<title>MarqueTally</title>
<link rel="stylesheet" href="https://fonts.googleapis.com/css2?family=Jost:wght@400;500;600&display=swap">
<style>
  :root {
    --brand-blue: #3594c6;
    --nav-grey: #5f5f5f;
    --white: #ffffff;
    --button-text: #6a6a6a;
    --button-border: #5a1634;
    --hero-top: #7a3a6c;
    --hero-mid: #8e4677;
    --hero-bottom: #a05083;
  }
  * { margin: 0; padding: 0; box-sizing: border-box; }
  html, body { width: 1200px; height: 640px; overflow: hidden; }
  body {
    position: relative;
    font-family: "Jost", "Century Gothic", sans-serif;
    background: var(--white);
  }
  .site-header {
    position: absolute; left: 0; top: 0;
    width: 1200px; height: 62px;
    background: var(--white);
    z-index: 2;
  }
  .brand {
    position: absolute; left: 88px; top: 16px;
    font-size: 22px; font-weight: 500;
    color: var(--brand-blue);
    letter-spacing: -0.3px;
  }
  .main-nav a {
    position: absolute; top: 22px;
    font-size: 14px; font-weight: 500;
    color: var(--nav-grey);
    text-decoration: none;
    letter-spacing: 0.4px;
  }
  .main-nav .about { left: 710px; color: var(--brand-blue); }
  .main-nav .about::after {
    content: ""; position: absolute; left: -2px; right: -2px; top: 25px;
    height: 3px; background: var(--brand-blue);
  }
  .main-nav .press { left: 815px; }
  .main-nav .contact { left: 884px; }
  .sign-in {
    position: absolute; left: 1026px; top: 18px;
    width: 86px; height: 30px;
    border: 1px dashed #777;
    border-bottom: 2px dotted #555;
    font-size: 13px; font-weight: 500;
    color: var(--nav-grey);
    text-align: center; line-height: 28px;
    letter-spacing: 0.4px;
  }
  .hero {
    position: absolute; left: 0; top: 62px;
    width: 1200px; height: 578px;
  }
  .hero-backdrop {
    position: absolute; inset: 0;
    background:
      radial-gradient(ellipse at 50% 45%, rgba(190,110,150,0.35), transparent 60%),
      linear-gradient(180deg, var(--hero-top), var(--hero-mid) 55%, var(--hero-bottom));
  }
  .hero-dots {
    position: absolute; left: 570px; top: 136px;
    width: 62px; height: 4px;
    background: radial-gradient(circle, var(--white) 1.2px, transparent 1.6px) 0 0 / 6.2px 4px repeat-x;
  }
  .hero-title {
    position: absolute; left: 0; top: 138px; width: 1200px;
    text-align: center;
    font-size: 110px; font-weight: 600;
    color: var(--white); line-height: 1;
    letter-spacing: 1px;
  }
  .hero-motto {
    position: absolute; left: 0; top: 278px; width: 1200px;
    text-align: center;
    font-size: 37px; font-weight: 500;
    color: var(--white); letter-spacing: 1px;
  }
  .signup-button {
    position: absolute; left: 436px; top: 352px;
    width: 329px; height: 69px;
    background: var(--white);
    border: 2px solid var(--button-border);
    font-size: 29px; font-weight: 500;
    color: var(--button-text);
    text-align: center; line-height: 65px;
    letter-spacing: 0.6px;
  }
</style>
</head>
<body>
  <header class="site-header">
    <div class="brand">MarqueTally</div>
    <nav class="main-nav">
      <a class="about" href="#">ABOUT US</a>
      <a class="press" href="#">PRESS</a>
      <a class="contact" href="#">CONTACT US</a>
    </nav>
    <div class="sign-in">SIGN IN</div>
  </header>
  <section class="hero">
    <div class="hero-backdrop" role="img" aria-label="Aerial view of a city skyline at dusk with tall towers, tinted purple"></div>
    <div class="hero-dots"></div>
    <h1 class="hero-title">MarqueTally</h1>
    <p class="hero-motto">OBSERVE NAVIGATE DECIDE</p>
    <div class="signup-button">SIGN UP NOW</div>
  </section>
</body>
</html>
```